Stationery Design Project

KT7 Staffing requires letterhead and business card designs for a company based in London. Just like the name, we're a management resourcing company, providing resources to third party companies. You can see www.kt7staffing-example.com for ideas on existing colour schemes and design concepts that have been implimented and agreed to. Ultimately the design should broadcast professionalism, safety and the concept of growth.

Target Market(s)

Financial institutes; friendly societies (All UK based)

Industry/Entity Type

Safety

Requirements
Must have
• Files produced should be print ready; and the text in them editable (eg address, name etc)

```html
<!DOCTYPE html>
<html lang="en">
<head>
<meta charset="utf-8">
<title>KT7 Staffing – Business Card</title>
<link href="https://fonts.googleapis.com/css2?family=Arimo:wght@400;700&display=swap" rel="stylesheet">
<style>
  :root {
    --teal: #1a9fb0;
    --teal-deep: #15899a;
    --teal-text: #1b8f9e;
    --grey-text: #6b6b6b;
    --rule-blue: #a9cfe0;
    --card-white: #ffffff;
    --decor-grey: #eeeeee;
  }
  * { margin: 0; padding: 0; box-sizing: border-box; }
  html, body {
    width: 1200px; height: 900px; overflow: hidden;
    background: #ffffff;
    font-family: "Arimo", Arial, sans-serif;
  }
  .canvas { position: relative; width: 1200px; height: 900px; }

  .card {
    position: absolute;
    box-shadow: 4px 6px 8px rgba(0,0,0,0.28);
    overflow: hidden;
  }

  /* Front */
  .card-front {
    left: 302px; top: 124px; width: 522px; height: 308px;
    background: var(--teal);
  }
  .front-decor {
    position: absolute; right: 0; top: 0; width: 250px; height: 308px;
    background: linear-gradient(120deg, rgba(21,137,154,0) 0%, rgba(21,137,154,0.55) 55%, var(--teal-deep) 100%);
  }
  .front-wordmark {
    position: absolute; left: 34px; top: 236px;
    color: #ffffff; font-weight: 700; font-size: 26px; letter-spacing: 0.5px;
  }

  /* Back */
  .card-back {
    left: 280px; top: 460px; width: 542px; height: 306px;
    background: var(--card-white);
  }
  .back-decor {
    position: absolute; right: 0; top: 0; width: 240px; height: 306px;
    background: linear-gradient(120deg, rgba(238,238,238,0) 0%, var(--decor-grey) 60%, #e6e6e6 100%);
  }
  .back-wordmark {
    position: absolute; left: 320px; top: 32px;
    color: var(--teal-text); font-weight: 700; font-size: 22px; letter-spacing: 0.5px;
  }
  .person { position: absolute; left: 56px; top: 100px; }
  .person-name { color: var(--teal-text); font-weight: 700; font-size: 28px; line-height: 30px; }
  .person-title {
    color: var(--grey-text); font-size: 9.5px; letter-spacing: 0.6px;
    text-transform: uppercase; margin-top: 4px;
  }
  .contact-list {
    position: absolute; left: 56px; top: 162px;
    color: var(--grey-text); font-size: 9.5px; line-height: 13px;
  }
  .contact-list .label { display: inline-block; width: 36px; }
  .web-list {
    position: absolute; left: 56px; top: 224px;
    color: var(--grey-text); font-size: 9.5px; line-height: 13px;
  }
  .divider {
    position: absolute; left: 294px; top: 106px; width: 1px; height: 138px;
    background: var(--rule-blue);
  }
  .address {
    position: absolute; left: 352px; top: 186px;
    color: var(--grey-text); font-size: 9.5px; line-height: 12px;
  }
  .address .company { color: var(--teal-text); font-weight: 700; }
</style>
</head>
<body>
<main class="canvas">
  <section class="card card-front" aria-label="Business card front">
    <div class="front-decor" role="img" aria-label="Faint brand decoration area"></div>
    <div class="front-wordmark">KT7 STAFFING</div>
  </section>

  <section class="card card-back" aria-label="Business card back">
    <div class="back-decor" role="img" aria-label="Faint brand decoration area"></div>
    <div class="back-wordmark">KT7 STAFFING</div>

    <div class="person">
      <div class="person-name">Daniel Hartley</div>
      <div class="person-title">Managing Director</div>
    </div>

    <div class="contact-list">
      <div><span class="label">Office:</span>+44 (0) 20 7946 0158</div>
      <div><span class="label">Fax:</span>+44 (0) 20 7946 0159</div>
      <div><span class="label">Mobile:</span>+44 (0) 7700 900 415</div>
      <div><span class="label">e-mail:</span>d.hartley@kt7staffing-example.com</div>
    </div>

    <div class="web-list">
      <div>info@kt7staffing-example.com</div>
      <div>www.kt7staffing-example.com</div>
    </div>

    <div class="divider"></div>

    <div class="address">
      <div class="company">KT7 Staffing Ltd.</div>
      <div>Harrow Court</div>
      <div>Mill Lane</div>
      <div>READING, RG1 4TP</div>
      <div>UNITED KINGDOM</div>
    </div>
  </section>
</main>
</body>
</html>
```